Business Card Design Project

Basic business card with minimal details. I just need company name, email & web address, telephone and my name.
I would like the back of the card to be grey with my logo & company name centred.

Target Market(s)

Architects
Builders
Property Developers

Industry/Entity Type

Business

Font styles to use
Sans Serif

Colors

Designer to choose colors to be used in the design.

Requirements
Must have
• Framewise Build
Marcus Helby - Director
M: 0427 593184
E: marcus@framewisebuild.com.au
W: www.framewisebuild.com.au
Should not have
• No other images or pictures

```html
<!DOCTYPE html>
<html lang="en">
<head>
<meta charset="utf-8">
<title>Framewise Build – Business Card</title>
<link rel="stylesheet" href="https://fonts.googleapis.com/css2?family=PT+Sans:wght@400;700&family=PT+Sans+Narrow:wght@700&display=swap">
<style>
  :root {
    --canvas-bg: #e8e4df;
    --card-bg: #242424;
    --card-shadow: rgba(0, 0, 0, 0.35);
    --text-grey: #5e6571;
    --contact-grey: #7b808a;
    --accent-crimson: #a3173b;
  }
  * { margin: 0; padding: 0; box-sizing: border-box; }
  html, body {
    width: 1200px;
    height: 900px;
    overflow: hidden;
    background: var(--canvas-bg);
  }
  .canvas {
    position: relative;
    width: 1200px;
    height: 900px;
  }
  .card {
    position: absolute;
    width: 681px;
    height: 410px;
    background: var(--card-bg);
    box-shadow: 0 6px 18px var(--card-shadow);
  }
  .card--front { left: 50px; top: 15px; }
  .card--back { left: 479px; top: 442px; }

  .holder {
    position: absolute;
    right: 64px;
    top: 58px;
    text-align: right;
  }
  .holder__name {
    font-family: "PT Sans Narrow", sans-serif;
    font-weight: 700;
    font-size: 24px;
    color: var(--text-grey);
    text-transform: uppercase;
    line-height: 1.05;
  }
  .holder__role {
    font-family: "PT Sans Narrow", sans-serif;
    font-weight: 700;
    font-size: 20px;
    color: var(--accent-crimson);
    font-variant: small-caps;
    line-height: 1.05;
  }

  .brand {
    display: flex;
    align-items: center;
    gap: 18px;
  }
  .brand__square {
    width: 22px;
    height: 22px;
    background: var(--accent-crimson);
  }
  .brand__name {
    font-family: "PT Sans", sans-serif;
    font-weight: 400;
    color: var(--text-grey);
    text-transform: uppercase;
    letter-spacing: 0.12em;
    white-space: nowrap;
  }
  .card--front .brand {
    position: absolute;
    left: 50px;
    top: 166px;
  }
  .card--front .brand__name { font-size: 34px; }

  .card--back .brand {
    position: absolute;
    left: 0;
    right: 0;
    top: 236px;
    justify-content: center;
  }
  .card--back .brand__square { width: 28px; height: 28px; }
  .card--back .brand__name { font-size: 40px; }

  .contacts {
    position: absolute;
    left: 50px;
    top: 262px;
    list-style: none;
  }
  .contacts__item {
    display: flex;
    align-items: center;
    gap: 9px;
    height: 27px;
    font-family: "PT Sans", sans-serif;
    font-size: 14px;
    color: var(--contact-grey);
  }
  .contacts__icon {
    width: 13px;
    height: 13px;
    fill: var(--accent-crimson);
    flex: none;
  }
</style>
</head>
<body>
<main class="canvas">
  <section class="card card--front" aria-label="Business card front">
    <div class="holder">
      <p class="holder__name">Marcus Helby</p>
      <p class="holder__role">Director</p>
    </div>
    <div class="brand">
      <span class="brand__square"></span>
      <span class="brand__name">Framewise Build</span>
    </div>
    <ul class="contacts">
      <li class="contacts__item">
        <svg class="contacts__icon" viewBox="0 0 16 16" aria-hidden="true"><path d="M4 1h3l1 4-2 1.5c.8 1.8 2 3 3.5 3.5L11 8l4 1v3c0 1.5-1 3-3 3C6 15 1 10 1 4c0-2 1.5-3 3-3z"/></svg>
        <span>0427 593184</span>
      </li>
      <li class="contacts__item">
        <svg class="contacts__icon" viewBox="0 0 16 16" aria-hidden="true"><circle cx="8" cy="8" r="7"/><path d="M1 8h14M8 1c-3 3.5-3 10.5 0 14M8 1c3 3.5 3 10.5 0 14" stroke="#242424" stroke-width="1.2" fill="none"/></svg>
        <span>www.framewisebuild.com.au</span>
      </li>
      <li class="contacts__item">
        <svg class="contacts__icon" viewBox="0 0 16 16" aria-hidden="true"><path d="M1 3h14v10H1z" fill="none" stroke="#a3173b" stroke-width="1.6"/><path d="M1 3l7 6 7-6" fill="none" stroke="#a3173b" stroke-width="1.6"/></svg>
        <span>marcus@framewisebuild.com.au</span>
      </li>
    </ul>
  </section>

  <section class="card card--back" aria-label="Business card back">
    <div class="brand">
      <span class="brand__square"></span>
      <span class="brand__name">Framewise Build</span>
    </div>
  </section>
</main>
</body>
</html>
```